Electrical Business Card Design

New electrical business targeting my local area
Installations
Repairs
Switchboards
TV / Vistacast / Antennas
Telephone
Data Networks
Audio Visual
Licence # 518427K
ABN 58316927405
I would like some white background, black writing, red, blue & green can be used
Designer discretion to be used on layout, colour placement & any images
Reason: To give designers more time, I thought 5 days wasn't enough
Please don't just create generic business cards................include personal details e.g. business name, contact name, ph #, email. Also include the things I do, licence # & abn (refer to brief for all details)
Thanks
Reason: Would like more designs & have now committed my payment, thank you
Industry/Entity Type
Electrical
Contact Information for Business Card
Korvane Electrical Services,
Gareth Pelling,
0438 571 963,
korvaneelectrical@wexmail.net.au,
My suburb is Ryde
Look and feel

```html
<!DOCTYPE html>
<html lang="en">
<head>
<meta charset="utf-8">
<title>Korvane Electrical Services – Business Card &amp; Logo</title>
<link rel="stylesheet" href="https://fonts.googleapis.com/css2?family=Arimo:wght@400&family=Tinos&display=swap">
<style>
  :root {
    --page: #ffffff;
    --card-front: #f4f4f4;
    --trim: #9a9a9a;
    --brand-blue: #0a63b5;
    --brand-green: #1fae4b;
    --back-blue: #0a93bd;
    --back-green: #09a24a;
    --ink-grey: #555555;
    --label-ink: #222222;
    --mark-light: #e2e2e2;
  }
  html, body { margin: 0; padding: 0; overflow: hidden; }
  body { width: 1200px; height: 1000px; background: var(--page); position: relative; font-family: "Arimo", Arial, sans-serif; }

  .sheet-label { position: absolute; font-family: "Tinos", "Times New Roman", serif; font-size: 8px; color: var(--label-ink); margin: 0; }
  .sheet-label--card { left: 78px; top: 86px; }
  .sheet-label--logo { left: 749px; top: 86px; }

  .card { position: absolute; left: 75px; width: 619px; height: 355px; box-sizing: border-box; }
  .card--front { top: 103px; background: var(--card-front); border: 1px dashed var(--trim); }
  .card--back { top: 548px; height: 353px; background: linear-gradient(115deg, var(--back-blue) 0%, var(--back-blue) 38%, var(--back-green) 62%, var(--back-green) 100%); }

  .brand { position: absolute; display: flex; align-items: center; white-space: nowrap; }
  .brand__dot { border-radius: 50%; flex: none; }
  .brand__name { display: flex; flex-direction: column; line-height: 1; font-weight: 400; }
  .brand__word { letter-spacing: 0.3px; }

  .brand--front { left: 342px; top: 172px; color: var(--brand-blue); }
  .brand--front .brand__dot { width: 52px; height: 52px; background: var(--brand-blue); margin-right: 5px; }
  .brand--front .brand__word { font-size: 36px; }
  .brand--front .brand__trade { font-size: 13.5px; letter-spacing: 1.5px; margin-top: 2px; }

  .brand--back { left: 23px; top: 296px; color: #ffffff; }
  .brand--back .brand__dot { width: 48px; height: 48px; background: var(--mark-light); margin-right: 3px; }
  .brand--back .brand__word { font-size: 34px; }
  .brand--back .brand__trade { font-size: 12.5px; letter-spacing: 1.6px; margin-top: 1px; }

  .brand--sheet { left: 743px; top: 125px; color: var(--brand-blue); }
  .brand--sheet .brand__dot { width: 80px; height: 80px; background: var(--brand-blue); margin-right: 7px; }
  .brand--sheet .brand__word { font-size: 56px; }
  .brand--sheet .brand__trade { font-size: 21px; letter-spacing: 2.4px; margin-top: 3px; }

  .services { position: absolute; left: 22px; top: 22px; margin: 0; padding: 0; list-style: none; font-size: 11px; line-height: 16px; color: var(--ink-grey); }
  .services__item::before { content: ""; display: inline-block; width: 5px; height: 5px; border-radius: 50%; background: var(--brand-green); margin-right: 7px; vertical-align: middle; }
  .credentials { position: absolute; left: 22px; bottom: 20px; margin: 0; font-size: 11px; line-height: 16px; color: var(--ink-grey); }
  .credentials__key { color: var(--brand-blue); }

  .contact { position: absolute; right: 10px; top: 268px; text-align: right; }
  .contact__name { margin: 0 0 10px; font-size: 18px; letter-spacing: 2.2px; color: var(--brand-blue); font-weight: 400; text-transform: uppercase; }
  .contact__line { margin: 0; font-size: 17px; color: var(--ink-grey); line-height: 20px; }
  .contact__key { color: var(--brand-green); }
</style>
</head>
<body>
  <p class="sheet-label sheet-label--card">Business Card</p>
  <p class="sheet-label sheet-label--logo">Logo Design</p>

  <section class="card card--front" aria-label="Business card front">
    <ul class="services">
      <li class="services__item">Installations</li>
      <li class="services__item">Repairs</li>
      <li class="services__item">Switchboards</li>
      <li class="services__item">TV / Vistacast / Antennas</li>
      <li class="services__item">Telephone</li>
      <li class="services__item">Data Networks</li>
      <li class="services__item">Audio Visual</li>
    </ul>
    <p class="credentials"><span class="credentials__key">Licence #</span> 518427K<br><span class="credentials__key">ABN</span> 58316927405</p>
    <div class="brand brand--front">
      <span class="brand__dot"></span>
      <span class="brand__name"><span class="brand__word">KORVANE</span><span class="brand__trade">ELECTRICAL SERVICES</span></span>
    </div>
    <div class="contact">
      <h2 class="contact__name">Gareth Pelling</h2>
      <p class="contact__line"><span class="contact__key">t</span> 0438 571 963</p>
      <p class="contact__line"><span class="contact__key">e</span> korvane@wexmail.net.au</p>
    </div>
  </section>

  <section class="card card--back" aria-label="Business card back">
    <div class="brand brand--back">
      <span class="brand__dot"></span>
      <span class="brand__name"><span class="brand__word">KORVANE</span><span class="brand__trade">ELECTRICAL SERVICES</span></span>
    </div>
  </section>

  <div class="brand brand--sheet" aria-label="Korvane Electrical Services logo">
    <span class="brand__dot"></span>
    <span class="brand__name"><span class="brand__word">KORVANE</span><span class="brand__trade">ELECTRICAL SERVICES</span></span>
  </div>
</body>
</html>
```